Bold Modern Creative Wine Label Needed for a Chardonnay

We need a modern, eye catching label, one that will appeal to millennials, but also attract the older more conservative crowd. We like the boldness of black on white but are open to your suggestions. Since the bottle type is a light green 'burgundy style' bottle, you should take that into account. The name of the brand is Vo`. The attached label is example of what we like very much. It is eye catching and bold and modern. Keep in mind that the bottle will be light green in color so black and white might not work so well. Use your creativity please! The label can be any size but needs to fit on this shape bottle. See attached photos. thanks!!

(Please no grapes or wine glasses or wine bottles featured on the label!)
Updates

Hi Designers, I just wanted to let you know that we received many great designs and we are sorting through them this week. The website is making it a bit difficult to create a 'poll' so this is taking longer than we expected. Thanks for all the great submissions!

```html
<!DOCTYPE html>
<html lang="en">
<head>
<meta charset="utf-8">
<title>Vo` Chardonnay 2018 – Label</title>
<link rel="stylesheet" href="https://fonts.googleapis.com/css2?family=Jost:wght@300;800&display=swap">
<style>
  :root {
    --backdrop: #d9d9d9;
    --label-paper: #f4f4f2;
    --ink: #1c1c1c;
    --label-edge: #cfcfcc;
  }
  html, body {
    margin: 0;
    padding: 0;
    width: 1200px;
    height: 900px;
    overflow: hidden;
    background: var(--backdrop);
  }
  .canvas {
    position: relative;
    width: 1200px;
    height: 900px;
    display: flex;
    align-items: center;
    justify-content: center;
  }
  .wine-label {
    position: relative;
    width: 620px;
    height: 640px;
    background: var(--label-paper);
    border: 1px solid var(--label-edge);
    box-sizing: border-box;
    font-family: "Jost", sans-serif;
    color: var(--ink);
  }
  .brand-name {
    position: absolute;
    left: 84px;
    top: 40px;
    margin: 0;
    font-weight: 300;
    font-size: 280px;
    line-height: 1;
    letter-spacing: -4px;
  }
  .stem-rule {
    position: absolute;
    left: 104px;
    top: 300px;
    width: 22px;
    height: 270px;
    background: var(--ink);
  }
  .varietal {
    position: absolute;
    left: 150px;
    top: 318px;
    margin: 0;
    font-weight: 800;
    font-size: 68px;
    line-height: 1;
    letter-spacing: 1px;
  }
  .vintage {
    position: absolute;
    left: 154px;
    top: 408px;
    margin: 0;
    font-weight: 300;
    font-size: 30px;
    letter-spacing: 0.9em;
  }
</style>
</head>
<body>
  <main class="canvas">
    <section class="wine-label" aria-label="Vo` Chardonnay 2018 wine label">
      <h1 class="brand-name">Vo`</h1>
      <div class="stem-rule"></div>
      <p class="varietal">chardonnay</p>
      <p class="vintage">2018</p>
    </section>
  </main>
</body>
</html>
```